Brisket Dwelling Review is a leading provider of residential appraisal and home inspection products in S

I need a business card/logo designed that obviously describes my business. We are a residential appraisal and home inspection company in Springfield, MO. We offer residential appraisals, home inspection, pest inspection and radon gas measurement. We have been in business for 18 years and hold state certified residential appraisal licenses and VORMEL certified home inspection licenses. I have a logo that I really like and will attach, but would be open to new suggestions. I like more modern designs than traditional and would like a two sided card with our services, licenses and qualifications on the back.

```html
<!DOCTYPE html>
<html lang="en">
<head>
<meta charset="utf-8">
<title>Brisket Dwelling Review — Business Card</title>
<link href="https://fonts.googleapis.com/css2?family=Arimo:wght@400;700&display=swap" rel="stylesheet">
<style>
  :root {
    --orange: #f7941d;
    --brown: #a17f57;
    --ink: #2b2b2b;
    --paper: #ffffff;
    --backdrop: #e9e4dc;
    --rule: #3a3a3a;
  }
  * { box-sizing: border-box; margin: 0; padding: 0; }
  html, body { width: 1200px; height: 858px; overflow: hidden; }
  body {
    background: var(--backdrop);
    font-family: "Arimo", Arial, sans-serif;
    color: var(--ink);
    position: relative;
  }
  .card {
    position: absolute;
    top: 280px;
    width: 525px;
    height: 300px;
    background: var(--paper);
    box-shadow: 0 6px 18px rgba(0,0,0,0.18);
    overflow: hidden;
  }
  .card--front { left: 50px; }
  .card--back { left: 625px; }

  /* Wordmark */
  .wordmark {
    display: flex;
    align-items: center;
    gap: 8px;
    font-weight: 700;
    color: var(--brown);
    line-height: 1.1;
  }
  .wordmark__square {
    width: 14px; height: 14px;
    background: var(--orange);
    flex: none;
  }

  /* Front */
  .front__top {
    position: absolute;
    inset: 0 0 108px 0;
  }
  .front__brand {
    position: absolute;
    left: 34px;
    top: 78px;
    width: 190px;
    font-size: 19px;
  }
  .front__divider {
    position: absolute;
    left: 248px;
    top: 32px;
    width: 1px;
    height: 136px;
    background: var(--rule);
  }
  .contacts {
    position: absolute;
    left: 272px;
    top: 40px;
    list-style: none;
    font-size: 15px;
    line-height: 22px;
  }
  .contacts li { display: flex; align-items: center; gap: 8px; }
  .contacts svg { width: 12px; height: 12px; flex: none; }
  .front__band {
    position: absolute;
    left: 0; right: 0; bottom: 0;
    height: 108px;
    background: var(--brown);
    padding: 16px 0;
  }
  .front__band-inner {
    height: 100%;
    background: var(--orange);
    display: flex;
    flex-direction: column;
    justify-content: center;
    align-items: center;
    font-size: 17px;
    line-height: 24px;
    color: #1e1e1e;
  }

  /* Back */
  .back__brand {
    position: absolute;
    right: 34px;
    top: 44px;
    font-size: 22px;
  }
  .back__tagline {
    position: absolute;
    right: 34px;
    top: 76px;
    width: 1px;
  }
  .services {
    position: absolute;
    top: 120px;
    list-style: none;
    font-size: 15px;
    line-height: 21px;
    color: #333;
  }
  .services--core { left: 34px; }
  .services--extra { left: 282px; }
  .services--extra li { display: flex; align-items: center; gap: 9px; }
  .services--extra svg { width: 10px; height: 10px; flex: none; }
</style>
</head>
<body>

<section class="card card--front" aria-label="Card front">
  <div class="front__top">
    <div class="wordmark front__brand">
      <span class="wordmark__square"></span>
      <span>Brisket Dwelling Review</span>
    </div>
    <div class="front__divider"></div>
    <ul class="contacts">
      <li>
        <svg viewBox="0 0 12 12" aria-hidden="true"><rect width="12" height="12" fill="var(--orange)"/><rect x="4" y="2" width="4" height="8" rx="0.8" fill="#fff"/></svg>
        555-214-7730
      </li>
      <li>
        <svg viewBox="0 0 12 12" aria-hidden="true"><rect width="12" height="12" fill="var(--orange)"/><path d="M3 3.2c.4-.6 1.3-.6 1.6 0l.5 1.1-.8.7c.4.9 1 1.6 1.9 2l.7-.8 1.1.5c.6.3.6 1.2 0 1.6-2.7 1.2-6.2-2.3-5-5.1z" fill="#fff"/></svg>
        555-398-1062
      </li>
      <li>
        <svg viewBox="0 0 12 12" aria-hidden="true"><rect width="12" height="12" fill="var(--orange)"/><rect x="2.5" y="5" width="7" height="4.5" fill="#fff"/><rect x="4" y="2.5" width="4" height="2.5" fill="#fff"/></svg>
        555-640-2285
      </li>
      <li>
        <svg viewBox="0 0 12 12" aria-hidden="true"><rect width="12" height="12" fill="var(--orange)"/><rect x="2.5" y="3.5" width="7" height="5" fill="#fff"/><path d="M2.5 3.5 6 6.5 9.5 3.5" fill="none" stroke="var(--orange)" stroke-width="0.8"/></svg>
        info@brisketdwellingreview.com
      </li>
    </ul>
  </div>
  <div class="front__band">
    <div class="front__band-inner">
      <span>Brisket Dwelling Review 4870 W Larkspur Avenue, Suite C</span>
      <span>Millbrook, MO 65999</span>
    </div>
  </div>
</section>

<section class="card card--back" aria-label="Card back">
  <div class="wordmark back__brand">
    <span class="wordmark__square"></span>
    <span>Brisket Dwelling Review</span>
  </div>
  <ul class="services services--core">
    <li>home inspection</li>
    <li>property inspection</li>
    <li>residential appraisal</li>
    <li>pest inspection</li>
    <li>radon measurement</li>
    <li>site inspection</li>
  </ul>
  <ul class="services services--extra">
    <li><svg viewBox="0 0 10 10" aria-hidden="true"><path d="M1 1 L5 9 L9 1 L7 1 L5 5 L3 1 Z" fill="var(--orange)"/></svg>thermal imaging</li>
    <li><svg viewBox="0 0 10 10" aria-hidden="true"><path d="M1 1 L5 9 L9 1 L7 1 L5 5 L3 1 Z" fill="var(--orange)"/></svg>mechanical inspection</li>
    <li><svg viewBox="0 0 10 10" aria-hidden="true"><path d="M1 1 L5 9 L9 1 L7 1 L5 5 L3 1 Z" fill="var(--orange)"/></svg>tax appeal</li>
    <li><svg viewBox="0 0 10 10" aria-hidden="true"><path d="M1 1 L5 9 L9 1 L7 1 L5 5 L3 1 Z" fill="var(--orange)"/></svg>asset evaluation</li>
    <li><svg viewBox="0 0 10 10" aria-hidden="true"><path d="M1 1 L5 9 L9 1 L7 1 L5 5 L3 1 Z" fill="var(--orange)"/></svg>energy audits</li>
  </ul>
</section>

</body>
</html>
```